Electrical & Communications Company Wordpress Themed Website Design

Hi everyone,

I need a wordpress themed website designed for a new company based in Sydney Australia called "TRELVEX". It delivers electrical and communication services to the domestic and commercial sectors.

It needs to be the FULL/COMPLETE wordpress theme! A clean and easy to use site.

Please guys take the time to look at these competitors sites:

www.quobble.com.au
www.zirconvoltworks.com.au
www.ubt.com.au
www.tallowwiring.com.au
www.wrightbergwire.com.au
www.gullivarwiremen.com.au

Please use these site for ideas only!!! we want to be original.

(If you would like to add electrical and communications to the logo that is O.K.)

Note: These logo's are registered trademarks of trelvex pty ltd.

Accreditation:

Bufo member (United cabling and signalling trades guild)

PLEASE CHECK THE WEB PLANNING LAYOUT BELOW FOR ROUGH IDEA

Have requested to increase payment to $400 and now guarantee payment!

Hi guys, forgot to mention i would like to see the business phone number prominently some where with a call to action.As we are a service business and need people to easly be able to see our contact number. Maybe top right courner but open to ideas. 

 Guys/Girls this is for a complete working word press theme that i can load up on the sever and access thru wordpress admin. Code etc

• - Logo Provided must be used
• - Themes and colours to be consisted with with brand
• - Fully customizable
• - Have a social share button from pinquo.com
• - Must be the full/complete theme for word press
• - zenpixbanks
• - contactform
• - would like orbe lumo charge bitfen displayed
• - Guarantee logo or something
• - Please don't waste your or our time submitting templates or copies of other sites original only!

```html
<!DOCTYPE html>
<html lang="en">
<head>
<meta charset="utf-8">
<title>Trelvex – Electrical &amp; Communications</title>
<link rel="stylesheet" href="https://fonts.googleapis.com/css2?family=Arimo:wght@400;700&family=Open+Sans:wght@400;600&display=swap">
<style>
:root{
  --page-blue:#1f5fae;
  --page-blue-dark:#0c3b7c;
  --nav-blue:#2a86d6;
  --nav-blue-dark:#0f4f96;
  --nav-active:#0b3f7a;
  --brand-red:#e3202a;
  --ink:#555;
  --ink-dark:#333;
  --heading-blue:#1a5fa6;
  --panel-border:#a9cdea;
  --panel-top:#ffffff;
  --panel-bottom:#d4ebfa;
  --white:#fff;
}
*{box-sizing:border-box;margin:0;padding:0}
html,body{width:1200px;height:1157px;overflow:hidden}
body{
  position:relative;
  font-family:"Arimo",Arial,sans-serif;
  background:linear-gradient(90deg,var(--page-blue-dark) 0%,var(--page-blue) 3%,#e9f4fc 3%,#e9f4fc 97%,var(--page-blue) 97%,var(--page-blue-dark) 100%);
}
.page{position:absolute;left:35px;top:0;width:1128px;height:1157px;background:var(--white)}
.abs{position:absolute}

/* header */
.header{left:0;top:0;width:1128px;height:156px;background:linear-gradient(#f4f9fd,#e6f1fa)}
.logo-box{left:22px;top:0;width:373px;height:146px;border-radius:0 0 14px 14px;
  background:linear-gradient(#fafafa,#d8d8d8);border:1px solid #c9c9c9;border-top:none;
  display:flex;align-items:center;justify-content:center;gap:14px}
.logo-mark{width:40px;height:40px;border-radius:50%;background:var(--brand-red)}
.logo-name{font-family:"Arimo",Arial,sans-serif;font-weight:700;font-size:50px;color:var(--brand-red);letter-spacing:1px}
.top-links{right:21px;top:12px;font-family:"Open Sans",sans-serif;font-size:16px;color:var(--heading-blue);white-space:nowrap}
.top-links a{color:var(--heading-blue);text-decoration:none}
.call-us{right:14px;top:32px;font-size:50px;white-space:nowrap}
.call-us .label{color:var(--brand-red)}
.call-us .number{color:#555}

/* nav */
.nav{left:0;top:159px;width:1128px;height:47px;background:linear-gradient(var(--nav-blue),var(--nav-blue-dark));
  font-family:"Open Sans",sans-serif;font-size:19px}
.nav a{position:absolute;top:0;color:var(--white);text-decoration:none;height:47px;line-height:47px;white-space:nowrap}
.nav a.active{background:var(--nav-active);padding:0 6px}

/* hero */
.hero{left:8px;top:213px;width:841px;height:354px;border-radius:14px;border:1px solid #8bb7da;overflow:hidden;
  background:radial-gradient(circle at 22% 40%,#ffffff 0%,#a9dcf7 18%,#3a8fd0 45%,#1d4d8c 80%)}
.hero-art{position:absolute;inset:0}
.hero-line{position:absolute;left:300px;width:410px;text-align:center;font-family:"Open Sans",sans-serif;font-size:22px;color:#111;white-space:nowrap}

/* side form */
.panel{border:1px solid var(--panel-border);background:linear-gradient(var(--panel-top),var(--panel-bottom))}
.contact{left:857px;top:213px;width:263px;height:354px}
.contact h2{position:absolute;left:12px;top:6px;width:240px;font-family:"Open Sans",sans-serif;font-weight:400;font-size:18px;line-height:25px;color:var(--heading-blue)}
.contact .photo{left:17px;top:61px;width:116px;height:129px;border:1px solid #888;background:linear-gradient(#f2c53a,#2f2f2f)}
.contact .avail{left:141px;top:62px;width:112px;font-size:12.5px;line-height:22px;color:var(--ink-dark)}
.field{left:17px;width:229px;height:27px;border:1px solid #444;background:var(--white);font-size:13px;color:#333;padding:5px 10px;white-space:nowrap}
.send{left:19px;top:313px;width:116px;height:36px;border:1px solid #155a9e;background:linear-gradient(#5db7f0,#1d6fc0);color:var(--white);font-family:"Open Sans",sans-serif;font-size:22px;text-align:center;line-height:34px}

/* content boxes */
.welcome{left:12px;top:579px;width:594px;height:317px}
.welcome h1{position:absolute;left:13px;top:14px;font-family:"Open Sans",sans-serif;font-weight:400;font-size:24px;color:var(--heading-blue);white-space:nowrap}
.welcome h1 span{color:var(--brand-red);font-size:37px}
.welcome p{position:absolute;left:6px;top:72px;width:580px;font-size:14.4px;line-height:27.6px;color:var(--ink);text-align:justify}
.box{top:579px;height:317px}
.box h2{position:absolute;left:0;top:6px;width:100%;text-align:center;font-size:19px;font-weight:700;color:var(--heading-blue);white-space:nowrap}
.box .pic{border:1px solid var(--panel-border)}
.box p{position:absolute;font-size:13.5px;line-height:21.5px;color:var(--ink-dark)}
.services{left:613px;width:250px}
.guarantee{left:870px;width:248px}
.btn{position:absolute;height:32px;width:115px;border:1px solid #155a9e;background:linear-gradient(#5db7f0,#1d6fc0);color:var(--white);font-size:15px;text-align:center;line-height:30px;white-space:nowrap}

/* badges */
.badges{left:12px;top:905px;width:1106px;height:152px}
.badge{top:9px;height:132px;border:1px solid var(--panel-border);background:var(--white);display:flex;align-items:center;justify-content:center}

/* footer */
.footer{left:0;top:1074px;width:1128px;height:83px;background:linear-gradient(var(--nav-blue),var(--page-blue-dark));color:var(--white);font-size:15.5px}
.footer .copy{left:27px;top:18px;white-space:nowrap}
.footer .links{left:27px;top:49px;white-space:nowrap}
.footer a{color:var(--white);text-decoration:none}
.card{top:20px;width:60px;height:42px;border-radius:5px;background:var(--white);border:1px solid #9fb9d4;display:flex;align-items:center;justify-content:center;font-size:11px;font-weight:700;color:var(--heading-blue);text-align:center;line-height:12px}
</style>
</head>
<body>
<div class="page">

  <header class="header abs">
    <div class="logo-box abs">
      <span class="logo-mark"></span>
      <span class="logo-name">TRELVEX</span>
    </div>
    <nav class="top-links abs"><a href="#">Home</a> | <a href="#">Contact us</a> | <a href="#">Careers</a></nav>
    <div class="call-us abs"><span class="label">Call us:</span> <span class="number">000-000-0000</span></div>
  </header>

  <nav class="nav abs">
    <a href="#" style="left:14px">Who we are</a>
    <a href="#" style="left:148px">Our Services</a>
    <a href="#" style="left:290px">Domestic</a>
    <a href="#" class="active" style="left:398px">Commercial sectors</a>
    <a href="#" style="left:616px">Our Experience</a>
    <a href="#" style="left:785px">Our Guarantee</a>
    <a href="#" style="left:948px">Client Satisfaction</a>
  </nav>

  <section class="hero abs">
    <div class="hero-art" role="img" aria-label="Glowing light bulb beside cut electrical cables on a blue background"></div>
    <p class="hero-line" style="top:80px">Don't worry your safety is our motto</p>
    <p class="hero-line" style="top:114px">we are always with you</p>
  </section>

  <aside class="contact panel abs">
    <h2>Call us now our Work Satisfaction Guarantee</h2>
    <div class="photo abs" role="img" aria-label="Electrician in a yellow hard hat holding a coil of cable"></div>
    <p class="avail abs">We are available<br>24 hours for all<br>Our Clients</p>
    <div class="field abs" style="top:197px">Enter Your Name</div>
    <div class="field abs" style="top:234px">Enter Your Email</div>
    <div class="field abs" style="top:275px">Enter Your Phone Number</div>
    <div class="send abs">SEND</div>
  </aside>

  <section class="welcome panel abs">
    <h1>WELCOME TO <span>TRELVEX</span></h1>
    <p>Our highly motivated team are rigorously trained and routinely tested for competency and compliance to ensure we meet stringent legislation requirements.Combine this with our company's comprehensive legislation and insurance, and you can be safe in the knowledge that Trelvex will deliver your electrical project to the highest possible standard that not only meets, but exceeds, today's stringent requirements.</p>
    <span class="btn" style="left:461px;top:271px">Read More</span>
  </section>

  <section class="box services panel abs">
    <h2>Our Services</h2>
    <div class="pic abs" style="left:23px;top:31px;width:204px;height:149px;background:linear-gradient(135deg,#f2c53a,#6a8fb3 60%,#e4e4e4)" role="img" aria-label="Grid of photos of electricians at work in hard hats"></div>
    <p style="left:5px;top:184px;width:240px">We provide a wide variety of services from electrical maintenance,repairs and installations across the domestic,commercial and industrial sectors</p>
    <span class="btn" style="left:126px;top:279px">Read More</span>
  </section>

  <section class="box guarantee panel abs">
    <h2>Our Guarantee</h2>
    <div class="pic abs" style="left:19px;top:31px;width:208px;height:156px;background:linear-gradient(135deg,#c9d6df,#f2c53a 45%,#3b4a5a)" role="img" aria-label="Smiling electrician giving a thumbs up beside a switchboard"></div>
    <p style="left:7px;top:207px;width:236px">We'll give you a guaranteed fixed price for any of your requirements before we even lift a spanner</p>
    <span class="btn" style="left:121px;top:279px">Read More</span>
  </section>

  <section class="badges panel abs" aria-label="Accreditations">
    <div class="badge abs" style="left:18px;width:180px"><svg width="110" height="110" viewBox="0 0 110 110"><circle cx="55" cy="55" r="50" fill="#e6edf5" stroke="#2d5f9a" stroke-width="3"/></svg></div>
    <div class="badge abs" style="left:238px;width:197px"><svg width="150" height="90" viewBox="0 0 150 90"><rect x="5" y="5" width="140" height="80" rx="6" fill="#eaf3dc" stroke="#5a9b35" stroke-width="3"/></svg></div>
    <div class="badge abs" style="left:482px;width:199px"><svg width="110" height="80" viewBox="0 0 110 80"><circle cx="55" cy="40" r="36" fill="#eef2f6" stroke="#1b3f6b" stroke-width="3"/></svg></div>
    <div class="badge abs" style="left:729px;width:198px"><svg width="140" height="100" viewBox="0 0 140 100"><rect x="5" y="5" width="130" height="90" fill="#1a3d8c"/></svg></div>
    <div class="badge abs" style="left:969px;width:116px"><svg width="70" height="60" viewBox="0 0 70 60"><rect x="5" y="5" width="60" height="50" fill="#f6dede" stroke="#d3262e" stroke-width="3"/></svg></div>
  </section>

  <footer class="footer abs">
    <p class="copy abs">© copy right 2010 Trelvex All Rights Reserved.</p>
    <p class="links abs"><a href="#">Home</a> | <a href="#">Who we are</a> | <a href="#">Our Services</a> | <a href="#">Contact Us</a></p>
    <span class="card abs" style="left:833px">Kestra</span>
    <span class="card abs" style="left:904px">orbe</span>
    <span class="card abs" style="left:975px">lumo charge</span>
    <span class="card abs" style="left:1046px">Notabank</span>
  </footer>

</div>
</body>
</html>
```